Design some Double Sided Business Cards

***FINAL FILES NEED TO BE SUBMITTED AS LAYERED PSD FILES***

Create a business card for a Home Repair company (logo attached). One side should include logo and contact info (ONLY Name, phone number & email) and the other side should list the services offered (put into 3 columns - 6 services in each column)

For your mockup use this contact info:
Rod Pemberton
555-472-9360
RodPemberton@[url removed, login to view]

Here are the list of services to add on the back (you can reorder these if need be for spacing reasons):
Flooring
Electric Repairs
Running Wires
Installing Interior/Exterior Lights
Appliance Repairs
Ac Repairs
Painting & Drywall
Counter Tops
Woodwork
Roofing
Plumbing
Tubs & Tile
Demolition
Renovations
Decks
Fences
Window Install & Window Repairs
Custom Interior/Exterior Installs & Designs

```html
<!DOCTYPE html>
<html lang="en">
<head>
<meta charset="UTF-8">
<title>Keystone Renovation – Business Cards</title>
<link href="https://fonts.googleapis.com/css2?family=Quicksand:wght@500;600;700&display=swap" rel="stylesheet">
<style>
  :root {
    --stage: #2b2d31;
    --maroon: #5a1417;
    --maroon-deep: #4a0f12;
    --accent-red: #c4262e;
    --paper: #ffffff;
    --tab-grey: #4a4a4d;
    --ink-light: #f4eeee;
  }
  * { margin: 0; padding: 0; box-sizing: border-box; }
  html, body {
    width: 1200px; height: 900px; overflow: hidden;
    background: var(--stage);
    font-family: "Quicksand", sans-serif;
  }
  .stage {
    position: relative; width: 1200px; height: 900px;
    display: flex; align-items: center; justify-content: center; gap: 60px;
  }
  .card {
    position: relative; overflow: hidden; flex: none;
    border-radius: 22px;
    box-shadow: 0 14px 30px rgba(0,0,0,.45);
  }

  /* Front (portrait) */
  .card-front { width: 330px; height: 540px; background: var(--maroon); }
  .card-front .split { position: absolute; inset: 0; width: 100%; height: 100%; }
  .brand {
    position: absolute; left: 0; right: 0; top: 110px;
    display: flex; align-items: center; justify-content: center; gap: 12px;
  }
  .brand-square { width: 34px; height: 34px; background: var(--maroon); flex: none; }
  .brand-name {
    color: var(--maroon); font-weight: 700; font-size: 22px;
    line-height: 1.15; letter-spacing: 1.5px; text-transform: uppercase;
  }
  .contact { position: absolute; left: 34px; right: 24px; top: 330px; color: var(--ink-light); }
  .contact-name { font-size: 24px; font-weight: 700; letter-spacing: .3px; }
  .contact-rule { width: 200px; height: 3px; background: var(--accent-red); margin: 8px 0 26px; }
  .contact-row {
    display: flex; align-items: center; gap: 12px;
    font-size: 14px; font-weight: 500; margin-bottom: 18px; white-space: nowrap;
  }
  .contact-row svg { flex: none; }

  /* Back (landscape) */
  .card-back {
    width: 560px; height: 330px;
    background: linear-gradient(160deg, var(--maroon) 0%, var(--maroon-deep) 100%);
  }
  .services-tab {
    position: absolute; top: 0; right: 40px; width: 190px; height: 54px;
    background: var(--tab-grey); border-radius: 0 0 12px 12px;
    color: var(--paper); font-size: 17px; font-weight: 600;
    display: flex; align-items: center; justify-content: center; letter-spacing: .5px;
  }
  .services { position: absolute; left: 30px; top: 36px; display: flex; gap: 30px; }
  .services-col { list-style: none; width: 210px; }
  .services-col.second { margin-top: 72px; width: 260px; }
  .services-col li {
    position: relative; padding-left: 14px;
    color: var(--ink-light); font-size: 12.5px; font-weight: 700; line-height: 1.45;
  }
  .services-col li::before {
    content: ""; position: absolute; left: 0; top: 6px;
    width: 6px; height: 6px; border-radius: 50%; background: var(--accent-red);
  }
</style>
</head>
<body>
<main class="stage">

  <section class="card card-front" aria-label="Business card front">
    <svg class="split" viewBox="0 0 330 540" preserveAspectRatio="none" aria-hidden="true">
      <path d="M0 0 H330 V200 C250 250 120 270 0 310 Z" fill="var(--paper)"/>
    </svg>
    <div class="brand">
      <span class="brand-square"></span>
      <span class="brand-name">Keystone<br>Renovation</span>
    </div>
    <div class="contact">
      <h1 class="contact-name">Rod Pemberton</h1>
      <div class="contact-rule"></div>
      <p class="contact-row">
        <svg width="18" height="18" viewBox="0 0 24 24" aria-hidden="true">
          <circle cx="12" cy="12" r="11" fill="none" stroke="var(--ink-light)" stroke-width="1.5"/>
          <path d="M8.5 6.5l2 2.5-1.2 1.4a7 7 0 0 0 4.3 4.3l1.4-1.2 2.5 2-1.2 1.8c-4.5-.5-8.5-4.5-9-9z" fill="var(--ink-light)"/>
        </svg>
        555-472-9360
      </p>
      <p class="contact-row">
        <svg width="18" height="18" viewBox="0 0 24 24" aria-hidden="true">
          <rect x="2" y="5" width="20" height="14" fill="none" stroke="var(--ink-light)" stroke-width="1.5"/>
          <path d="M2 5l10 8 10-8M2 19l7-7M22 19l-7-7" fill="none" stroke="var(--ink-light)" stroke-width="1.5"/>
        </svg>
        RodPemberton@homefixpros.com
      </p>
    </div>
  </section>

  <section class="card card-back" aria-label="Business card back">
    <div class="services-tab">Our services</div>
    <div class="services">
      <ul class="services-col">
        <li>Flooring</li>
        <li>Electric Repairs</li>
        <li>Running Wires</li>
        <li>Installing Interior/Exterior Lights</li>
        <li>Appliance Repairs</li>
        <li>Ac Repairs</li>
        <li>Painting &amp; Drywall</li>
        <li>Counter Tops</li>
        <li>Woodwork</li>
      </ul>
      <ul class="services-col second">
        <li>Roofing</li>
        <li>Plumbing</li>
        <li>Tubs &amp; Tile</li>
        <li>Demolition</li>
        <li>Renovations</li>
        <li>Decks</li>
        <li>Fences</li>
        <li>Window Install &amp; Window Repairs</li>
        <li>Custom Interior/Exterior Installs &amp; Designs</li>
      </ul>
    </div>
  </section>

</main>
</body>
</html>
```